Business Stationery - New Business card design

We are looking for some new business stationery, including business cards (double sided), compliment slips & letterheads for our offices in the UK, Ireland, North Carolina (US) & our Holdings company.

We are open to all ideas; however we are ideally looking for something that does not look corporate.

Our website is www.tallowmerefolk.com – this is the style of branding that we are currently using.

Here is some of the information that should be included;

Business Cards

Front
Logo
Name – Dominic Furnival
Job Title - Director
Direct line number - +353 (0)1 684 2710
Office number - +353 (0)1 692 4150
Email address – d.furnival@tallowmf.com
Website address – www.tallowmerefolk.com

Back
Logo
‘Specialists in IT Recruitment’
LinkedIn – Tallowmere Folk Partners
Twitter - @tallowhires
An image included – possibly ‘Image 1’ attached?

Letterheads & Compliment slips

UK (A4 size)
Logo
Phone numbers for the various offices;
London: +44 (0)20 7158 6240
Belfast: +44 (0)28 9186 3370
Dublin: +353 (0)1 692 4150
Raleigh, NC: +1 919 462 7300
Address: 2nd Floor, 84 Malvern Row, London W1C 7QZ
Email: info@tallowmf.com
Website: www.tallowmerefolk.com
Social media icons for LinkedIn & Twitter
Tallowmere Folk Partners Registered in England & Wales No. 8315726 VAT No. 871402396

Ireland (A4 size)
Logo
Address: 3-5 Lantern Street, Dublin 2 D02 KW81, Ireland
Email: info@tallowmf.com
Tallowmere Folk Partners (Ireland) Registered in Ireland No. 642093 VAT No. 5817320KK

USA (letter size)

Logo
Address: 845 N. Pemberly Street, Raleigh, North Carolina 27605, United States
Email: info@tallowmf.com
Tallowmere Folk Partners Inc. Registered in the State of North Carolina No. 2936410

Holdings (A4 size)

Logo
Address: 17 Quillon Street, Belfast BT27JD
Email: info@tallowmf.com
Tallowmere Folk Partners (Holdings) Ltd Registered in Northern Ireland No. NI735208

Target Market(s)

IT Professionals

Industry/Entity Type

It Professional

Contact Information for Business Card

Front
Logo
Name – Dominic Furnival
Job Title - Director

Back
Logo
Twitter - @tallowhires

```html
<!DOCTYPE html>
<html lang="en">
<head>
<meta charset="utf-8">
<title>Tallowmere Folk Partners – Stationery</title>
<link rel="stylesheet" href="https://fonts.googleapis.com/css2?family=Roboto:wght@400;500&display=swap">
<style>
  :root {
    --backdrop: #7d7d7d;
    --paper: #ffffff;
    --brand-blue: #1a5aa6;
    --brand-green: #5aa52a;
    --body-grey: #555555;
    --fold-grey: #d6d6d6;
  }
  * { margin: 0; padding: 0; box-sizing: border-box; }
  html, body { width: 1200px; height: 931px; overflow: hidden; }
  body {
    background: var(--backdrop);
    font-family: "Roboto", Arial, sans-serif;
    position: relative;
  }
  .sheet {
    position: absolute;
    background: var(--paper);
  }
  .wordmark {
    position: absolute;
    color: var(--brand-blue);
    font-weight: 500;
    white-space: nowrap;
    letter-spacing: 0.2px;
  }

  /* Letterhead */
  .letterhead { left: 115px; top: 102px; width: 508px; height: 718px; }
  .letterhead .wordmark { left: 42px; top: 53px; font-size: 12px; }
  .office-lines {
    position: absolute; left: 350px; top: 48px;
    border-left: 1px solid var(--body-grey);
    padding-left: 5px;
    font-size: 8.4px; line-height: 10.8px; color: var(--body-grey);
  }
  .office-lines b { color: var(--brand-blue); font-weight: 500; }
  .letter-footer {
    position: absolute; left: 55px; top: 647px; width: 505px;
    font-size: 8.2px; color: var(--body-grey);
  }
  .footer-contact {
    padding-bottom: 3px;
    border-bottom: 1px solid var(--brand-green);
    width: 394px;
    white-space: nowrap;
  }
  .footer-reg { margin-top: 5px; white-space: nowrap; position: relative; width: 394px; }
  .social-dots { position: absolute; right: 2px; top: 0; display: flex; gap: 3px; }
  .social-dots span {
    width: 10px; height: 10px; border-radius: 50%; background: var(--brand-green);
  }

  /* Envelope */
  .envelope { left: 663px; top: 414px; width: 413px; height: 184px; }
  .envelope svg { position: absolute; left: 0; top: 0; }
  .envelope .wordmark { left: 0; width: 413px; text-align: center; top: 42px; font-size: 9px; }

  /* Compliment slip */
  .comp-slip { left: 660px; top: 635px; width: 417px; height: 185px; }
  .comp-slip .wordmark { left: 24px; top: 28px; font-size: 10px; }
  .slip-address {
    position: absolute; left: 24px; top: 132px;
    font-size: 8.4px; line-height: 10.8px; color: var(--body-grey);
  }
  .slip-greeting {
    position: absolute; right: 36px; top: 150px;
    font-size: 15px; color: var(--brand-blue);
  }
  .slip-greeting .accent { color: var(--brand-green); }
</style>
</head>
<body>

  <section class="sheet letterhead">
    <div class="wordmark">Tallowmere Folk Partners</div>
    <div class="office-lines">
      <div><b>London:</b> +44 (0)20 7158 6240</div>
      <div><b>Belfast:</b> +44 (0)28 9186 3370</div>
      <div><b>Dublin:</b> +353 (0)1 692 4150</div>
      <div><b>Raleigh, NC:</b> +1 919 462 7300</div>
    </div>
    <div class="letter-footer">
      <div class="footer-contact">2nd Floor, 84 Malvern Row, London W1C 7QZ &nbsp;|&nbsp; info@tallowmf.com &nbsp;|&nbsp; www.tallowmerefolk.com</div>
      <div class="footer-reg">Tallowmere Folk Partners Registered in England &amp; Wales No. 8315726 | VAT No. 871402396
        <div class="social-dots"><span></span><span></span></div>
      </div>
    </div>
  </section>

  <section class="sheet envelope">
    <svg width="413" height="184" viewBox="0 0 413 184">
      <path d="M3 178 L140 80 M410 178 L280 82" stroke="var(--fold-grey)" stroke-width="0.8" fill="none"/>
      <path d="M6 10 L176 95 Q216 116 254 95 L408 8" stroke="#c4c4c4" stroke-width="1.2" fill="none"/>
    </svg>
    <div class="wordmark">Tallowmere Folk Partners</div>
  </section>

  <section class="sheet comp-slip">
    <div class="wordmark">Tallowmere Folk Partners</div>
    <div class="slip-address">
      <div>31847 Amberly Hollow</div>
      <div>Drive #512</div>
      <div>Fernlea, CA 91642</div>
    </div>
    <div class="slip-greeting">With <span class="accent">Compliments</span></div>
  </section>

</body>
</html>
```